Blue Harbor Business Cards

Name Tomas Welbridge
Title Mortgage Originator
Phone (800) 614-2290 x32
Direct (571) 362-0471
Email twelbridge@blueharborhomeloans.com
NMLS #1847362
Name Lena Ortiz
Title Mortgage Originator
Location (800) 614-2290 x55
Direct (440) 276-5190
Email lortiz@blueharborhomeloans.com
NMLS #2739418
Name Desmond Holloway-Finch
Title Mortgage Originator
Location (800) 614-2290 x56
Direct (202) 634-1975
Email dhollowayfinch@blueharborhomeloans.com
NMLS #2784530
Name Rosalyn Whitaker
Title Mortgage Originator
Location (800) 614-2290 x57
Direct (240) 358-6621
Email rwhitaker@blueharborhomeloans.com
NMLS #2491086
Name Gwen Holbrook
Title Mortgage Originator
Location (800) 614-2290 x58
Direct (540) 716-2384
Email gholbrook@blueharborhomeloans.com
NMLS #2438617
Name Ravi Dunmore
Title Mortgage Originator
Location (800) 614-2290 x59
Direct (240) 563-8827
Email rdunmore@blueharborhomeloans.com
NMLS #2597142
Name Ivy Marlow
Title Mortgage Originator
Location (800) 614-2290 x60
Direct (202) 479-3306
Email ivy@ivyfindshomes.com
NMLS #2718394
Contact Information for Business Card
Name Tomas Welbridge Title Mortgage Originator Phone (800) 614-2290 x32 Direct (571) 362-0471 Email twelbridge@blueharborhomeloans.com NMLS #1847362 Name Lena Ortiz Title Mortgage Originator Location (800) 614-2290 x55 Direct (440) 276-5190 Email lortiz@blueharborhomeloans.com NMLS #2739418 Name Desmond Holloway-Finch Title Mortgage Originator Location (800) 614-2290 x56 Direct (202) 634-1975 Email dhollowayfinch@blueharborhomeloans.com NMLS #2784530 Name Rosalyn Whitaker Title Mortgage Originator Location (800) 614-2290 x57 Direct (240) 358-6621 Email rwhitaker@blueharborhomeloans.com NMLS #2491086 Name Gwen Holbrook Title Mortgage Originator Location (800) 614-2290 x58 Direct (540) 716-2384 Email gholbrook@blueharborhomeloans.com NMLS #2438617 Name Ravi Dunmore Title Mortgage Originator Location (800) 614-2290 x59 Direct (240) 563-8827 Email rdunmore@blueharborhomeloans.com NMLS #2597142 Name Ivy Marlow Title Mortgage Originator Location (800) 614-2290 x60 Direct (202) 479-3306 Email ivy@ivyfindshomes.com NMLS #2718394
Look and feel
Each slider illustrates characteristics of the customer's brand and the style your logo design should communicate.

```html
<!DOCTYPE html>
<html lang="en">
<head>
<meta charset="utf-8">
<title>Blue Harbor Business Card – Tomas Welbridge</title>
<link rel="stylesheet" href="https://fonts.googleapis.com/css2?family=Montserrat:wght@700&family=Lato:wght@400;700&display=swap">
<style>
  :root {
    --backdrop: #808080;
    --card-red: #9b1c20;
    --accent-gold: #fdc22f;
    --text-light: #ffffff;
    --text-dark: #1a1a1a;
    --photo-top: #e6e6e3;
    --photo-bottom: #8dbf6a;
  }
  * { margin: 0; padding: 0; box-sizing: border-box; }
  html, body {
    width: 1200px; height: 1000px; overflow: hidden;
    background: var(--backdrop);
  }
  .canvas { position: relative; width: 1200px; height: 1000px; }
  .card {
    position: absolute; left: 26px; top: 172px;
    width: 1149px; height: 657px;
    background: var(--card-red);
    border-radius: 28px;
    overflow: hidden;
  }
  .edge-bar {
    position: absolute; top: 56px; width: 11px; height: 545px;
    background: var(--accent-gold);
  }
  .edge-bar.left { left: 0; border-radius: 0 6px 6px 0; }
  .edge-bar.right { right: 0; border-radius: 6px 0 0 6px; }
  .portrait-frame {
    position: absolute; left: 101px; top: 106px;
    width: 393px; height: 427px;
    border: 1.5px solid var(--text-light);
  }
  .portrait {
    position: absolute; left: 13px; top: 12px;
    width: 366px; height: 400px;
    background: linear-gradient(180deg, var(--photo-top) 0%, var(--photo-top) 45%, var(--photo-bottom) 100%);
  }
  .details {
    position: absolute; left: 530px; top: 0; width: 548px;
    text-align: center; color: var(--text-light);
    font-family: "Lato", sans-serif;
  }
  .name {
    position: absolute; left: 0; right: 0; top: 106px;
    font-family: "Montserrat", sans-serif; font-weight: 700;
    font-size: 49px; letter-spacing: 0.5px; line-height: 1;
    text-transform: uppercase;
  }
  .title {
    position: absolute; left: 0; right: 0; top: 162px;
    font-size: 30px; line-height: 1;
  }
  .contact-icons {
    position: absolute; left: 0; right: 0; top: 244px;
    display: flex; justify-content: center;
  }
  .contact-line {
    position: absolute; left: 0; right: 0;
    font-size: 30px; line-height: 1;
  }
  .contact-line.office { top: 304px; }
  .contact-line.direct { top: 354px; }
  .contact-line.email { top: 402px; font-size: 29px; }
  .nmls-badge {
    position: absolute; left: 144px; top: 476px;
    width: 260px; height: 46px; border-radius: 23px;
    background: var(--accent-gold); color: var(--text-dark);
    font-weight: 700; font-size: 24px;
    display: flex; align-items: center; justify-content: center;
  }
</style>
</head>
<body>
<div class="canvas">
  <div class="card">
    <div class="edge-bar left"></div>
    <div class="edge-bar right"></div>

    <div class="portrait-frame">
      <div class="portrait" role="img" aria-label="Headshot portrait of the loan originator"></div>
    </div>

    <div class="details">
      <h1 class="name">Tomas Welbridge</h1>
      <p class="title">Mortgage Originator</p>

      <div class="contact-icons">
        <svg width="222" height="36" viewBox="0 0 222 36" fill="none" stroke="#fdc22f" stroke-width="2">
          <line x1="0" y1="18" x2="38" y2="18" stroke-width="3"/>
          <rect x="48" y="1" width="34" height="34" rx="5"/>
          <rect x="59" y="8" width="12" height="20" rx="2"/>
          <line x1="63" y1="24" x2="67" y2="24"/>
          <rect x="93" y="1" width="34" height="34" rx="5"/>
          <path d="M100 15 q10 -8 20 0 l-2 3 h-3 v-3 h-10 v3 h-3 z" fill="#fdc22f"/>
          <rect x="103" y="18" width="14" height="9" rx="1"/>
          <rect x="137" y="1" width="34" height="34" rx="5"/>
          <path d="M143 18 l22 -9 l-5 20 l-6 -6 z" fill="#fdc22f" stroke-linejoin="round"/>
          <line x1="184" y1="18" x2="222" y2="18" stroke-width="3"/>
        </svg>
      </div>

      <p class="contact-line office">(800) 614-2290 x32</p>
      <p class="contact-line direct">(571) 362-0471</p>
      <p class="contact-line email">twelbridge@blueharborhomeloans.com</p>

      <div class="nmls-badge">NMLS #1847362</div>
    </div>
  </div>
</div>
</body>
</html>
```